Lift display layouts for global brand

We need display layouts for different sizes and applications of display. All layouts must include an arrow and floor position number. I will upload some basic examples. We want these to look modern and really eye-catching but suitable for the space it is meant for.

By "layout" we mean design specifically created for the space - including arrow, floor number, widgets / background graphics etc.
Display type ONE 15" (1024 x 768 pixels)
a. Hotel theme layout (logo, floor position, arrow and simple weather widget) [Landscape]
b. Layout displaying live TV news broadcast or similar [Landscape]
Display type TWO 10.4” (800 x 600 pixels)
a. Shopping centre layout + shop advert in main space [Landscape]
b. Office tenant standard layout + business logo in main space [Portrait]
c. Spa / Leisure Centre Layout [Landscape]
Display type 38” (1920 x 540 pixels)
a. Airport/Train station layout + flight/train departure information in main space [Landscape]
b. Restaurant layout + Menu in main space [Portrait]
c. Shopping Centre layout + Centre map in main space [Landscape]
Display type 21.5” (1920 x 1080 pixels)
a. Skyscraper layout + lift buttons and building history text [Portrait]
Display type 7” (800x480)
a. Simple lift position indicator arrow and floor [Landscape]
b. Lift position indicator with arrow and showing pictogram (Alarm, Maintenance or similar) [Landscape]

```html
<!DOCTYPE html>
<html lang="en">
<head>
<meta charset="utf-8">
<title>Lift Display – Hotel Floor Indicator</title>
<link rel="stylesheet" href="https://fonts.googleapis.com/css2?family=Montserrat:wght@200;300;400;500&display=swap">
<style>
  :root {
    --panel-top: #e0560f;
    --panel-mid: #c8321c;
    --panel-bottom: #7a1030;
    --accent-orange: #f5a623;
    --accent-gold: #f39c12;
    --band-crimson: #b8173d;
    --text-white: #ffffff;
    --logo-blue: #2f6db5;
    --photo-light: #d9c9b0;
    --photo-mid: #8c7d6c;
    --photo-dark: #3e3631;
  }
  * { margin: 0; padding: 0; box-sizing: border-box; }
  html, body { width: 1200px; height: 900px; overflow: hidden; background: #000; }
  body { font-family: "Montserrat", sans-serif; color: var(--text-white); }

  .display {
    position: relative;
    width: 1200px;
    height: 900px;
    overflow: hidden;
  }

  .room-photo {
    position: absolute;
    inset: 0;
    background:
      radial-gradient(ellipse at 88% 30%, #fff6e2 0%, rgba(255,240,210,0.7) 22%, rgba(255,240,210,0) 48%),
      linear-gradient(180deg, #6d655d 0%, var(--photo-mid) 30%, var(--photo-light) 55%, #5a4a3d 78%, var(--photo-dark) 100%);
  }

  .info-panel {
    position: absolute;
    left: 0; top: 0;
    width: 451px;
    height: 900px;
    background: linear-gradient(180deg, var(--panel-top) 0%, #d8441a 38%, var(--panel-mid) 60%, var(--panel-bottom) 100%);
    opacity: 0.96;
  }

  .direction-arrow {
    position: absolute;
    left: 126px; top: 87px;
    width: 172px; height: 172px;
  }

  .floor-number {
    position: absolute;
    left: 0; width: 422px;
    top: 340px;
    text-align: center;
    font-weight: 200;
    font-size: 205px;
    line-height: 1;
    letter-spacing: -4px;
  }

  .weather {
    position: absolute;
    left: 66px; top: 704px;
    display: flex;
    align-items: center;
    gap: 24px;
  }
  .weather-icon { width: 122px; height: 84px; }
  .weather-details { padding-top: 2px; }
  .weather-temp {
    font-size: 21px;
    font-weight: 400;
    padding-bottom: 6px;
    border-bottom: 1.5px solid var(--accent-gold);
    width: 154px;
  }
  .weather-temp sup { font-size: 12px; }
  .weather-condition, .weather-humidity {
    font-size: 17px;
    color: var(--accent-orange);
    line-height: 1.25;
  }
  .weather-condition { margin-top: 6px; }
  .weather-humidity span { color: var(--text-white); }

  .date-band {
    position: absolute;
    left: 18px; top: 814px;
    width: 375px; height: 45px;
    background: linear-gradient(90deg, rgba(184,23,61,0) 0%, var(--band-crimson) 18%, var(--band-crimson) 82%, rgba(184,23,61,0) 100%);
    display: flex; align-items: center; justify-content: center;
    font-size: 21px;
    font-weight: 400;
  }
  .date-band sup { font-size: 12px; }

  .hotel-badge {
    position: absolute;
    left: 870px; top: 688px;
    width: 264px; height: 264px;
    border-radius: 50%;
    background: #ffffff;
    display: flex; justify-content: center;
    padding-top: 150px;
  }
  .hotel-name {
    font-size: 24px;
    font-weight: 500;
    color: var(--logo-blue);
    white-space: nowrap;
  }
</style>
</head>
<body>
  <main class="display">
    <div class="room-photo" role="img" aria-label="Photo of a hotel room with a bed and folded towels, a couple with luggage looking out of a bright window"></div>

    <section class="info-panel">
      <svg class="direction-arrow" viewBox="0 0 172 172" aria-label="Going up">
        <circle cx="86" cy="86" r="86" fill="#f5a623"/>
        <circle cx="86" cy="86" r="63" fill="none" stroke="#ffffff" stroke-width="9"/>
        <path d="M86 126 V50 M56 80 L86 50 L116 80" fill="none" stroke="#ffffff" stroke-width="9" stroke-linecap="round" stroke-linejoin="round"/>
      </svg>

      <div class="floor-number">18</div>

      <div class="weather">
        <svg class="weather-icon" viewBox="0 0 122 84" aria-label="Partly cloudy">
          <g stroke="#f5b50a" stroke-width="3" stroke-linecap="round">
            <line x1="32" y1="2" x2="32" y2="10"/>
            <line x1="8" y1="26" x2="16" y2="26"/>
            <line x1="15" y1="9" x2="21" y2="15"/>
            <line x1="49" y1="9" x2="43" y2="15"/>
            <line x1="15" y1="43" x2="21" y2="37"/>
          </g>
          <circle cx="32" cy="27" r="15" fill="#f7c416"/>
          <path d="M20 80 H104 a16 16 0 0 0 0 -32 a26 26 0 0 0 -48 -10 a18 18 0 0 0 -26 12 a15 15 0 0 0 -10 30 z" fill="#ffffff"/>
          <path d="M62 80 H104 a16 16 0 0 0 0 -32 a26 26 0 0 0 -42 -14 z" fill="#eeeeee"/>
        </svg>
        <div class="weather-details">
          <div class="weather-temp">25<sup>0</sup> C / 76<sup>0</sup>F</div>
          <div class="weather-condition">Partly Cloudy</div>
          <div class="weather-humidity">Humidity <span>61%</span></div>
        </div>
      </div>

      <div class="date-band">May 15<sup>th</sup>, Monday</div>
    </section>

    <div class="hotel-badge">
      <span class="hotel-name">Seabreeze Hotel</span>
    </div>
  </main>
</body>
</html>
```